■レイアウトの希望について
◎2カラムで、必要に応じて上ナビも入れてください。
※全体の左右を970pxで、ナビの左右サイズを300pxでお願いします。
◎写真やイラストなどのイメージ画像は、最低1点以上入れてください。(有料画像も可)
※現サイトのイラストは自由に使用ください。

■内容について
◎サイト名のロゴは現行のものでなく新たにご提案ください。
※フォントを使用したものでOKです。
◎ヘッダーはスマホサイズになった場合のことも考えて作成してください。
※サイト名の周りは適当にキャッチを入れていただくか、文字を○○○○の形で入れてもかまいません。
◎トップページに入れる文章はできていますが、文字数が少ないのでバランスが悪ければ○○○○の形でプラスしてください。
◎ナビに入れるタイトルはページ構成から抜き出して入れてください。
※上ナビも入れる場合は項目をご提案ください。(左右ナビと変えてもダブってもOK)
※新聞奨学金を目立たせたいので、ナビを工夫されても良いかと思われます。
◎文章とページ構成は以下からダウンロードしてください。
http://www.qx5.co.jp/rmt.zip
基本的にはお任せですが、派手な色やくすんだ色は避けてください。(バランスの良い、落ち着いた色が希望)
納品ファイルは、JPG形式 (.jpg)またはPNG形式 (.png)のいずれかひとつと、イラストレーター形式 (.ai) またはフォトショップ形式 (.psd) のいずれかひとつの、計2ファイルに変更させていただきます。
申し訳ございませんが、ご了承ください。
提案の締め切り日を2日間延ばして6月20日にしました。

第一希望の新聞奨学金ページへの誘導方法がうまく、その他のアイデアも多くいただきました。
それに加え、全体のバランスや色使いが好みだったので、決めさせていただきました。
また、修正依頼などもすぐに対応いただき、助かりました。

多くのご提案をいただき、ありがとうございました。
結局は主観的な好みで決めさせていただきましたが、迷ったご提案も数点ありました。
なお、締切日ギリギリのご提案は、修正依頼が出せないので、良いご提案も見送らせていただいたものもありました。

```html
<!DOCTYPE html>
<html lang="ja">
<head>
<meta charset="utf-8">
<title>奨学金ガイド</title>
<link href="https://fonts.googleapis.com/css2?family=Noto+Sans+JP:wght@400;500;700&display=swap" rel="stylesheet">
<style>
:root{
  --teal:#26a28b;
  --teal-dark:#1d8572;
  --teal-pale:#e8f5f1;
  --teal-line:#bfe3da;
  --ink:#333;
  --muted:#666;
  --white:#fff;
  --photo-a:#d9e6e3;
  --photo-b:#b8cfca;
}
*{box-sizing:border-box;margin:0;padding:0}
html,body{width:1200px;height:2840px;overflow:hidden}
body{font-family:"Noto Sans JP",sans-serif;color:var(--ink);background:var(--white);font-size:14px;line-height:1.8;position:relative}
.wrap{width:1120px;margin:0 auto;position:relative}

/* header */
.site-header{height:140px;border-top:6px solid var(--teal)}
.site-header .wrap{display:flex;justify-content:space-between;padding-top:14px}
.brand .catch{font-size:13px;color:var(--muted)}
.brand .name{font-size:32px;font-weight:700;color:var(--teal);line-height:1.3}
.header-right{display:flex;gap:16px}
.util{font-size:13px;color:var(--muted);text-align:right}
.util span{padding:0 8px;border-left:1px solid #ccc}
.util span:first-child{border:0}
.gnav{display:flex;gap:10px;margin-top:18px}
.gnav a{display:block;width:150px;padding:10px 0;text-align:center;border:2px solid var(--teal);border-radius:6px;color:var(--teal);font-weight:700;text-decoration:none;font-size:15px}
.req-mini{width:150px;height:110px;background:var(--teal);color:var(--white);border-radius:6px;padding:10px 8px;text-align:center}
.req-mini .t{font-weight:700;font-size:17px;line-height:1.5}
.req-mini .s{font-size:10px;white-space:nowrap;line-height:1.6}
.req-mini .b{background:var(--white);color:var(--teal);font-weight:700;font-size:18px;margin-top:6px;letter-spacing:4px;border-radius:4px;line-height:1.7}

/* hero */
.hero{height:360px;background:var(--teal-pale)}
.hero .wrap{display:flex;height:100%}
.hero-text{flex:1;padding-top:40px}
.hero-text h1{font-size:36px;color:var(--teal);margin-bottom:28px}
.hero-text .lead{background:var(--white);border:2px solid var(--teal-line);border-radius:8px;padding:20px 24px;width:600px;font-size:15px}
.hero-photo{width:440px;height:100%;background:linear-gradient(135deg,var(--photo-a),var(--photo-b))}

/* columns */
.columns{display:flex;gap:30px;padding-top:20px}
.side{width:300px}
.main{width:790px}

.ad{border:3px solid var(--teal);border-radius:8px;overflow:hidden;margin-bottom:20px}
.ad .photo{height:150px;background:linear-gradient(135deg,#f4e8d8,#c8ded8);display:flex;align-items:center;padding-left:16px}
.ad .photo span{font-size:26px;font-weight:700;color:var(--teal);line-height:1.4}
.ad .cta{padding:14px;text-align:center}
.ad .cta .t{font-size:22px;font-weight:700;color:var(--teal)}
.ad .cta .s{font-size:12px;color:var(--muted)}
.ad .cta .b{margin-top:8px;background:var(--teal);color:var(--white);font-size:24px;font-weight:700;letter-spacing:8px;border-radius:6px;padding:4px 0}

.snav{border:1px solid var(--teal-line);margin-bottom:20px}
.snav li{list-style:none;height:42px;line-height:42px;padding-left:30px;border-bottom:1px solid var(--teal-line);font-size:14px;position:relative}
.snav li::before{content:"";position:absolute;left:14px;top:17px;border:5px solid transparent;border-left-color:var(--teal)}
.snav li.h{background:var(--teal);color:var(--white);font-weight:700;padding-left:16px}
.snav li.h::before{display:none}

.orgs{border:2px solid var(--teal);border-radius:6px;padding:12px;margin-bottom:20px}
.orgs h3{background:var(--teal);color:var(--white);text-align:center;font-size:15px;margin:-12px -12px 12px;padding:6px}
.orgs .grid{display:grid;grid-template-columns:1fr 1fr;gap:8px}
.orgs .grid span{border:1px solid var(--teal);text-align:center;font-size:13px;padding:6px 0;color:var(--teal-dark);white-space:nowrap}

.sec{margin-bottom:34px}
.sec h2{font-size:22px;color:var(--teal);border-bottom:3px solid var(--teal);padding-bottom:4px;margin-bottom:16px}
.sec p{margin-bottom:14px;font-size:15px}

.feature{display:flex;gap:20px;margin-bottom:34px}
.feature .card{flex:1;border:3px solid var(--teal);border-radius:8px;padding:20px}
.feature .card h3{text-align:center;color:var(--teal);font-size:22px;border-bottom:2px dotted var(--teal);padding-bottom:8px;margin-bottom:12px}
.feature .card .pic{height:120px;background:linear-gradient(135deg,var(--photo-a),var(--photo-b));margin-top:12px}
.feature .panel{width:330px}
.feature .panel li{list-style:none;background:var(--teal);color:var(--white);font-weight:700;padding:8px 16px;margin-bottom:2px;font-size:14px}
.feature .panel .orgs{margin-top:10px}

/* footer */
.site-footer{position:absolute;bottom:0;left:0;width:1200px;height:110px}
.fnav{background:var(--teal);color:var(--white);text-align:center;font-size:13px;padding:10px 0;line-height:20px}
.fnav span{padding:0 14px;border-left:1px solid rgba(255,255,255,.6)}
.fnav span:first-child{border:0}
.copy{text-align:center;font-size:12px;color:var(--muted);padding:30px 0 0;line-height:20px}
</style>
</head>
<body>
<header class="site-header">
  <div class="wrap">
    <div class="brand">
      <p class="catch">奨学金制度がよくわかるサイト</p>
      <p class="name">奨学金ガイド</p>
    </div>
    <div class="header-right">
      <div>
        <p class="util"><span>よくある質問</span><span>運営会社について</span><span>サイトマップ</span></p>
        <nav class="gnav"><a>借りる奨学金</a><a>働く奨学金</a><a>もらう奨学金</a></nav>
      </div>
      <div class="req-mini">
        <p class="t">新聞奨学会</p>
        <p class="s">パンフレットのお申し込み</p>
        <p class="b">資料請求</p>
      </div>
    </div>
  </div>
</header>

<section class="hero">
  <div class="wrap">
    <div class="hero-text">
      <h1>奨学金を知って上手に活用しよう!</h1>
      <p class="lead">「奨学金」は、経済的な理由や家庭の事情で「進学が難しい方」に向け、学費の貸与や給付を行う制度です。現在、多くの学生が奨学金制度を利用して、高校や専門学校・大学・大学院・海外の学校に進学しています。<br>「学費が足りない」と進学を諦める前に、自分に合う奨学金制度を見つけてみましょう。</p>
    </div>
    <div class="hero-photo" role="img" aria-label="本を読む学生の写真"></div>
  </div>
</section>

<div class="wrap columns">
  <aside class="side">
    <div class="ad">
      <div class="photo" role="img" aria-label="笑顔の学生の写真"><span>なりたい自分に<br>なるために</span></div>
      <div class="cta"><p class="s">学費・生活費を支援</p><p class="t">新聞奨学会</p><p class="s">パンフレットのお申し込み</p><p class="b">資料請求</p></div>
    </div>
    <ul class="snav">
      <li class="h">奨学金とは</li>
      <li>いろいろな奨学金</li>
      <li>誰が利用できるの？</li>
      <li>奨学金の使い道と利用時期</li>
      <li>奨学金のメリット・デメリット</li>
      <li class="h">奨学金の種類</li>
      <li>借りる「奨学金」</li>
      <li>働く「奨学金」</li>
      <li>もらう「奨学金」</li>
      <li class="h">奨学金の借り方</li>
      <li>奨学金の申請方法</li>
      <li>奨学金の選び方</li>
      <li>利用開始時期と窓口について</li>
      <li>保証制度について</li>
      <li>奨学金の利用について</li>
      <li>口座と合格の関係</li>
      <li class="h">奨学金の返済方法</li>
      <li>返済期間について</li>
      <li>繰り上げ返済のメリット</li>
      <li>返済が難しい場合</li>
      <li>奨学金の返済方法</li>
      <li>奨学金の返済</li>
      <li class="h">よくある質問</li>
      <li class="h">リンク集</li>
    </ul>
    <div class="orgs">
      <h3>全国新聞奨学会一覧</h3>
      <div class="grid"><span>東都奨学会</span><span>北辰育英会</span><span>青葉育英奨学会</span><span>若葉育英奨学会</span><span>港北奨学会</span><span>中央育英会</span></div>
    </div>
    <div class="ad">
      <div class="cta"><p class="s">学費・生活費を支援</p><p class="t">新聞奨学会</p><p class="s">パンフレットのお申し込み</p><p class="b">資料請求</p></div>
    </div>
  </aside>

  <main class="main">
    <section class="sec">
      <h2>奨学金制度のしくみ</h2>
      <p>奨学金制度は、国や地方自治体、民間団体のほか、学校単位でも独自の奨学金制度を設けています。各奨学金の申し込み基準や審査をクリアすれば、誰でも1度学に必要な金額の援助を受けることができます。</p>
      <p>このほかにも、学生の能力に合わせた奨学金制度、交通災害遺児のための奨学金、海外留学のための奨学金制度があります。</p>
    </section>
    <section class="sec">
      <h2>給付方法は二種類</h2>
      <p>奨学金制度は、大きく分けて二つに分類できます。一つ目は、貸与（たいよ）と呼ばれる給付の方法で、名称の通り学費を借りる（奨学金制度です。二つ目は、給付（きゅうふ）と呼ばれる方法で、返済の必要がない奨学金制度です。</p>
      <p>「貸与型奨学金制度」も、貸し付け利息が付くもの（有利子）と、利息の付かない（無利子）の二種類が存在します。</p>
    </section>
    <div class="feature">
      <div class="card">
        <h3>新聞奨学会</h3>
        <p>新聞社による奨学金制度です。販売店で新聞配達、集金などの仕事をすることで、新聞社から奨学金や給与が支給されます。純に経済的な負担がかかずに自立した生活が送れます。</p>
        <p>奨学金や仕事内容は新聞社により異なるので、志望校の学費や学習時間と照らし合わせて選んでみましょう。</p>
        <div class="pic" role="img" aria-label="新聞配達をする学生の写真"></div>
      </div>
      <div class="panel">
        <ul>
          <li>新聞奨学会とは</li>
          <li>申し込み方法</li>
          <li>新聞奨学会のメリット</li>
          <li>全国新聞奨学会一覧</li>
        </ul>
        <div class="orgs">
          <div class="grid"><span>東都奨学会</span><span>北辰育英会</span><span>青葉育英奨学会</span><span>若葉育英奨学会</span><span>港北奨学会</span><span>中央育英会</span></div>
        </div>
        <div class="ad"><div class="cta"><p class="t">新聞奨学会</p><p class="b">資料請求</p></div></div>
      </div>
    </div>
    <section class="sec">
      <h2>奨学金の借り方</h2>
      <p>まずは、自分の目的に合う給付制度（奨学金）を見つけましょう。各奨学金の「応募要項」を確認し、必要書類を準備してから奨学金の窓口に申し込みを行ってください。奨学金の審査に通ると、必要な学費のサポートが受けられるようになります。</p>
    </section>
    <section class="sec">
      <h2>奨学金の返済方法</h2>
      <p>奨学金の返済は、学校の卒業後に返済する制度と、学業と両立して働きながら返済する制度があります。また、給付（きゅうふ）型の奨学金であれば、返済する義務はありません。</p>
    </section>
  </main>
</div>

<footer class="site-footer">
  <p class="fnav"><span>よくある質問</span><span>リンク集</span><span>お問い合わせ</span><span>運営会社について</span><span>サイトマップ</span></p>
  <p class="copy">Copyright © 奨学金ガイド All Rights Reserved.</p>
</footer>
</body>
</html>
```